Simple landing page/Web presence for boutique Fund Manager, Brellow Funds Management

We need a website presence for our funds management business. All we need is a simple landing page with some "text" about us and a link /button to our Fund Due diligence portal. the "text" we would like to see is: "Brellow Funds Management Pty Ltd. Its Trustee is Tindale Fund Services Ltd - also based in Sydney. Tindale is the holder of an Australian Financial Services License (no.731052) whilst Brellow Funds Management operates under a Corporate Authorised Representation from Tindale."

We have the attached logo

```html
<!DOCTYPE html>
<html lang="en">
<head>
<meta charset="utf-8">
<title>Brellow Funds Management</title>
<link rel="stylesheet" href="https://fonts.googleapis.com/css2?family=Josefin+Sans:wght@600&family=Montserrat:wght@300;400;500;600&display=swap">
<style>
  :root {
    --brand-blue: #2399d6;
    --ink: #0d0d0d;
    --paper: #ffffff;
    --stage: #f4f6f8;
    --line: #9a9a9a;
    --footer: #0a0a0a;
    --footer-text: #e8e8e8;
  }
  * { box-sizing: border-box; margin: 0; padding: 0; }
  html, body { width: 1012px; height: 1200px; overflow: hidden; }
  body {
    background: var(--stage);
    font-family: "Montserrat", sans-serif;
    color: var(--ink);
    position: relative;
  }

  /* Brand name block */
  .brand-name {
    position: absolute; left: 0; top: 150px; width: 1012px;
    display: flex; align-items: center; justify-content: center; gap: 14px;
    font-family: "Montserrat", sans-serif; font-weight: 600; font-size: 34px;
    color: var(--ink);
  }
  .brand-name__mark { width: 22px; height: 22px; background: var(--ink); }

  /* Landing page */
  .site {
    position: absolute; left: 0; top: 300px; width: 1012px; height: 600px;
    background: var(--paper); overflow: hidden;
    box-shadow: 0 10px 30px rgba(0,0,0,0.08);
  }
  .site-header__logo {
    position: absolute; left: 77px; top: 36px;
    display: flex; align-items: center; gap: 8px;
    font-weight: 600; font-size: 16px; color: var(--ink);
  }
  .site-header__mark { width: 12px; height: 12px; background: var(--ink); }
  .site-nav {
    position: absolute; left: 430px; top: 40px;
    display: flex; gap: 27px; font-weight: 300; font-size: 13px;
  }
  .site-nav a { color: var(--ink); text-decoration: none; }
  .site-nav a.is-active { color: var(--brand-blue); }
  .site-search { position: absolute; left: 899px; top: 32px; }

  .hero-art {
    position: absolute; left: 500px; top: 80px; width: 512px; height: 395px;
    background: radial-gradient(ellipse at 60% 55%, #7cc3ea 0%, #b9dcf1 45%, #eef6fb 80%, #ffffff 100%);
  }
  .hero-skyline {
    position: absolute; left: 0; top: 330px; width: 500px; height: 145px;
    background: linear-gradient(180deg, rgba(240,242,244,0) 0%, #f2f3f5 100%);
  }
  .hero {
    position: absolute; left: 77px; top: 112px; width: 410px;
    display: flex; flex-direction: column; align-items: flex-start;
  }
  .hero__title {
    font-family: "Josefin Sans", sans-serif; font-weight: 600; font-size: 25px;
    letter-spacing: 0.5px; text-transform: uppercase; color: var(--ink);
    margin-bottom: 12px; white-space: nowrap;
  }
  .hero__intro {
    font-weight: 500; font-size: 14px; line-height: 24px; letter-spacing: 0.2px;
  }
  .hero__intro em { font-style: normal; color: var(--brand-blue); }
  .hero__licence {
    margin-top: 8px; font-weight: 400; font-size: 12px; line-height: 19px; color: #333;
  }
  .hero__cta {
    margin-top: 18px; width: 193px; height: 41px;
    border-radius: 21px; background: var(--brand-blue); color: #fff;
    font-weight: 500; font-size: 13.5px; text-decoration: none;
    display: flex; align-items: center; justify-content: center;
    box-shadow: 0 3px 6px rgba(0,0,0,0.2);
  }

  .site-footer { position: absolute; left: 0; top: 412px; width: 1012px; height: 188px; }
  .site-footer__legal {
    position: absolute; left: 0; top: 161px; width: 1012px; text-align: center;
    font-size: 9.5px; color: var(--footer-text);
  }
</style>
</head>
<body>
  <header class="brand-name">
    <span class="brand-name__mark"></span>
    <span>Brellow Funds Management</span>
  </header>

  <main class="site">
    <div class="hero-skyline" role="img" aria-label="Faint line drawing of the Sydney skyline"></div>
    <div class="hero-art" role="img" aria-label="Illustration of an investor standing among stacks of coins with a rising arrow and a money bag"></div>

    <div class="site-header__logo">
      <span class="site-header__mark"></span>
      <span>Brellow Funds Management</span>
    </div>
    <nav class="site-nav">
      <a class="is-active" href="#">Home</a>
      <a href="#">About Us</a>
      <a href="#">Services</a>
      <a href="#">Blog</a>
      <a href="#">Contact Us</a>
    </nav>
    <svg class="site-search" width="34" height="34" viewBox="0 0 34 34" aria-label="Search">
      <circle cx="17" cy="17" r="17" fill="var(--brand-blue)"/>
      <circle cx="15.5" cy="15.5" r="4" fill="none" stroke="#fff" stroke-width="2"/>
      <line x1="18.5" y1="18.5" x2="22" y2="22" stroke="#fff" stroke-width="2.2" stroke-linecap="round"/>
    </svg>

    <section class="hero">
      <h1 class="hero__title">Brellow Funds Management</h1>
      <p class="hero__intro">Brellow Funds Management Pty Ltd. Its Trustee is Tindale Fund Services Ltd - <em>also based in Sydney</em></p>
      <p class="hero__licence">Tindale is the holder of an Australian Financial Services License (no.731052) whilst Brellow Funds Management operates under a Corporate Authorised Representation from Tindale.</p>
      <a class="hero__cta" href="#">Due Diligence Portal</a>
    </section>

    <footer class="site-footer">
      <svg width="1012" height="188" viewBox="0 0 1012 188">
        <path d="M0 63 L410 63 C455 63 470 40 490 22 C502 12 516 12 528 22 C548 40 563 63 608 63 L1012 63 L1012 188 L0 188 Z" fill="var(--footer)"/>
        <circle cx="509" cy="49" r="15" fill="none" stroke="#555" stroke-width="1"/>
        <polyline points="504,47 509,52 514,47" fill="none" stroke="#bbb" stroke-width="1.6" stroke-linecap="round"/>
        <g fill="none" stroke="#ffffff" stroke-width="1">
          <circle cx="440" cy="131" r="12"/>
          <circle cx="484" cy="131" r="12"/>
          <circle cx="528" cy="131" r="12"/>
          <circle cx="572" cy="131" r="12"/>
        </g>
      </svg>
      <p class="site-footer__legal">Copyrights © 2020, The Company Name.All rights reserved &nbsp;|&nbsp; Privacy policy &nbsp;|&nbsp; Site Map &nbsp;|&nbsp; Disclaimer &nbsp;|&nbsp; Terms of use</p>
    </footer>
  </main>
</body>
</html>
```